Business card design

Hi,
I need to have a business card design based on the current logo.
If competitive I not put it out to everyone.

It can be single of double sided

Target Market(s)

Food businesses

Industry/Entity Type

Food Manufacturing

Contact Information for Business Card

Details will on card will be as follows Name = Marcus Pell Email = Marcus@BrimKitchens.com.au Phone = 0418562307 Address = 57 Tallowmere Road , Marrowvale Heights QLD 4199 Australia

Font styles to use
Other font styles liked:
• based on two fonts - Adelle & Museo

Requirements
Must have
• Based on the on switch concept

```html
<!DOCTYPE html>
<html lang="en">
<head>
<meta charset="utf-8">
<title>Brim Kitchens – Business Card</title>
<link rel="stylesheet" href="https://fonts.googleapis.com/css2?family=Poppins:wght@500;600&family=Zilla+Slab:wght@500&display=swap">
<style>
  :root {
    --backdrop: #dcdcdc;
    --brand-red: #e0304a;
    --card-white: #f2f2f0;
    --ink: #3a2a2c;
  }
  * { margin: 0; padding: 0; box-sizing: border-box; }
  html, body { width: 1200px; height: 1200px; overflow: hidden; background: var(--backdrop); }
  .canvas { position: relative; width: 1200px; height: 1200px; font-family: "Poppins", sans-serif; }

  .card {
    position: absolute; left: 242px; width: 703px; height: 400px;
    border-radius: 200px; overflow: hidden;
  }
  .card--front { top: 170px; background: var(--brand-red); }
  .card--back { top: 629px; background: var(--card-white); }

  .switch-ring {
    position: absolute; width: 330px; height: 330px; border-radius: 50%;
    display: flex; align-items: center; justify-content: center;
  }
  .card--front .switch-ring { left: 337px; top: 35px; background: var(--card-white); }
  .card--front .switch-knob { width: 220px; height: 220px; border-radius: 50%; background: var(--brand-red); }
  .card--back .switch-ring { left: 37px; top: 36px; background: var(--brand-red); }
  .card--back .switch-knob {
    width: 220px; height: 220px; border-radius: 50%; background: var(--card-white);
    display: flex; align-items: center; justify-content: center;
  }
  .person-name { color: var(--brand-red); font-weight: 600; font-size: 21px; letter-spacing: 0.3px; }

  .brand { position: absolute; right: 88px; top: 73px; text-align: right; }
  .brand-line { display: flex; align-items: center; gap: 8px; justify-content: flex-end; }
  .brand-dot { width: 22px; height: 22px; border-radius: 50%; background: var(--brand-red); }
  .brand-name { font-weight: 600; font-size: 24px; color: var(--ink); line-height: 1; letter-spacing: 0.5px; }
  .brand-tagline { font-family: "Zilla Slab", serif; font-weight: 500; font-size: 10px; color: var(--ink); margin-top: 3px; }

  .contact {
    position: absolute; left: 400px; width: 240px; top: 152px;
    text-align: center; color: var(--ink); font-weight: 500;
  }
  .contact-icon { display: block; margin: 0 auto; }
  .address { font-size: 16px; line-height: 20px; margin-top: 4px; white-space: nowrap; }
  .contact-icons { display: flex; justify-content: center; gap: 8px; margin-top: 6px; }
  .email { font-size: 16px; margin-top: 4px; white-space: nowrap; margin-left: -30px; margin-right: -30px; }
  .phone { font-size: 17px; margin-top: 2px; }
</style>
</head>
<body>
<div class="canvas">
  <section class="card card--front" aria-label="Card front">
    <div class="switch-ring"><div class="switch-knob"></div></div>
  </section>

  <section class="card card--back" aria-label="Card back">
    <div class="switch-ring">
      <div class="switch-knob"><span class="person-name">MARCUS PELL</span></div>
    </div>

    <div class="brand">
      <div class="brand-line">
        <span class="brand-dot"></span>
        <span class="brand-name">BRIMKITCHENS</span>
      </div>
      <div class="brand-tagline">Kitchen Supply Made Simple</div>
    </div>

    <div class="contact">
      <svg class="contact-icon" width="18" height="28" viewBox="0 0 18 28" aria-hidden="true">
        <path d="M9 1a7 7 0 0 0-7 7c0 5 7 12 7 12s7-7 7-12a7 7 0 0 0-7-7z" fill="none" stroke="var(--brand-red)" stroke-width="2.2"/>
        <circle cx="9" cy="8" r="2.4" fill="var(--brand-red)"/>
        <rect x="1" y="25" width="16" height="2" fill="var(--brand-red)"/>
      </svg>
      <p class="address">57 Tallowmere Road ,<br>Marrowvale Heights<br>QLD 4199 Australia</p>
      <div class="contact-icons">
        <svg width="18" height="18" viewBox="0 0 18 18" aria-hidden="true">
          <circle cx="9" cy="9" r="9" fill="var(--brand-red)"/>
          <rect x="4.5" y="5.5" width="9" height="7" rx="1" fill="none" stroke="#fff" stroke-width="1.4"/>
          <path d="M4.8 6l4.2 3.5L13.2 6" fill="none" stroke="#fff" stroke-width="1.4"/>
        </svg>
        <svg width="18" height="18" viewBox="0 0 18 18" aria-hidden="true">
          <circle cx="9" cy="9" r="9" fill="var(--brand-red)"/>
          <path d="M6 4.5l2 2.2-1.1 1.4a7 7 0 0 0 3 3l1.4-1.1 2.2 2-1.2 1.6c-3.6-.4-6.4-3.2-7-7z" fill="#fff"/>
        </svg>
      </div>
      <p class="email">Marcus@BrimKitchens.com.au</p>
      <p class="phone">(041) 856 2307</p>
    </div>
  </section>
</div>
</body>
</html>
```